Tour agency for FIT and groups need a business card design

We need a business card design for a tour agency company that is based in Perth called" BRISK NO", we aim to provide customise, unique and seamless travel arrangement for FIT and groups. We serve both high profile businessperson, government authorities, business partners, executives and investors. The name card should be more professional looking.
Updates

Project Deadline Extended Reason: Have some changes that needed to make, director will be back to office on Monday, sorry for the inconvenience cause. Added Saturday, May 6, 2017

Target Market(s)

High profile businessperson, government authorities, business partners, executives and investors.

Industry/Entity Type

Tourism

Contact Information for Business Card

Brisk NO
Level 1, 214 Marlowe Avenue, Dunreath NO, 6120
www.briskno.com.au

Font styles to use
Serif

Colors

Designer to choose colors to be used in the design.

Requirements
Must have
• My project must have a company logo
Nice to have
• a more professional and solid yet friendly name card design. We may want to include chinese name in the name card as well. Edge of the card can be filled with gold and we think that transparent name cards are interesting.

```html
<!DOCTYPE html>
<html lang="en">
<head>
<meta charset="utf-8">
<title>Brisk NO – Business Card</title>
<link href="https://fonts.googleapis.com/css2?family=Open+Sans:wght@400;600&display=swap" rel="stylesheet">
<style>
  :root {
    --backdrop: #4a423e;
    --card-black: #0d0d0d;
    --text-light: #e6e6e6;
    --accent-blue: #2fa8e0;
    --mark-grey: #b9b9b9;
    --foil-silver: #d4d4d4;
  }
  * { margin: 0; padding: 0; box-sizing: border-box; }
  html, body { width: 1200px; height: 900px; overflow: hidden; }
  body {
    background: var(--backdrop);
    font-family: "Open Sans", Arial, sans-serif;
    position: relative;
  }
  .card {
    position: absolute;
    top: 300px;
    width: 520px;
    height: 300px;
    background: var(--card-black);
    border-radius: 4px;
    box-shadow: 0 10px 30px rgba(0,0,0,0.35);
  }
  .card--contact { left: 50px; }
  .card--brand { left: 630px; }

  .brand-block {
    position: absolute;
    left: 50px;
    top: 150px;
    display: flex;
    align-items: center;
    gap: 12px;
  }
  .brand-dot {
    width: 18px; height: 18px;
    border-radius: 50%;
    background: var(--mark-grey);
  }
  .brand-name {
    color: var(--mark-grey);
    font-size: 30px;
    font-weight: 600;
  }

  .contact {
    position: absolute;
    left: 270px;
    top: 62px;
    color: var(--text-light);
    font-size: 14px;
    line-height: 1.3;
  }
  .contact__name {
    color: var(--accent-blue);
    font-size: 19px;
    font-weight: 600;
    line-height: 1.1;
  }
  .contact__role { margin-bottom: 14px; }
  .contact__address { margin-bottom: 12px; }
  .contact__line { display: flex; align-items: center; gap: 8px; }
  .contact__line svg { width: 11px; height: 11px; flex: none; }

  .brand-wordmark {
    position: absolute;
    inset: 0;
    display: flex;
    align-items: center;
    justify-content: center;
    gap: 14px;
  }
  .brand-wordmark .brand-dot { background: var(--foil-silver); width: 20px; height: 20px; }
  .brand-wordmark .brand-name { color: var(--foil-silver); font-size: 44px; }
</style>
</head>
<body>
  <section class="card card--contact">
    <div class="brand-block">
      <span class="brand-dot"></span>
      <span class="brand-name">Brisk NO</span>
    </div>
    <div class="contact">
      <p class="contact__name">Daniel Hartley</p>
      <p class="contact__role">Managing Director</p>
      <p class="contact__address">Level 1, 214 Marlowe Avenue,<br>Dunreath NO, 6120</p>
      <p class="contact__line">
        <svg viewBox="0 0 12 12" aria-hidden="true"><path fill="var(--accent-blue)" d="M2.5 1l2 2-1 1.3c.7 1.5 1.8 2.6 3.2 3.2L8 6.5l2 2-1.2 1.8C4.5 10 1.8 7 1.6 2.4z"/></svg>
        044-987 654 321
      </p>
      <p class="contact__line">
        <svg viewBox="0 0 12 12" aria-hidden="true"><rect x="1" y="2.5" width="10" height="7" fill="var(--accent-blue)"/><path d="M1 2.5l5 4 5-4" stroke="var(--card-black)" fill="none"/></svg>
        info@briskno.com.au
      </p>
      <p class="contact__line">
        <svg viewBox="0 0 12 12" aria-hidden="true"><path d="M5 7l3-3M4 5.5L2.5 7a1.8 1.8 0 002.5 2.5L6.5 8M8 6.5L9.5 5A1.8 1.8 0 007 2.5L5.5 4" stroke="var(--accent-blue)" stroke-width="1.4" fill="none"/></svg>
        www.briskno.com.au
      </p>
    </div>
  </section>

  <section class="card card--brand">
    <div class="brand-wordmark">
      <span class="brand-dot"></span>
      <span class="brand-name">Brisk NO</span>
    </div>
  </section>
</body>
</html>
```